PowerPoint Design Project

We are looking for a corporate presentation design (example content provided on approximately 30 slides).

The design will be a corporate design for our brand: GVRU
Continental Voyage Planners Union
For brand colours, requirements and logo look at: www.gvru-sample.org/media
or check the attached documents. We need to incorporate logo and brand but we are happy to refresh the palette. Attached please also find designs and colour palette of our new website-presentation should complement these.

You are also free to use photos from events some of which can be found here:
http://www.socialpage-example.com/pages/Continental-Voyage-Planners-Union/507194362810935?sk=photos_stream

Most important:
-PROFESSIONAL AUDIENCE-PROFESSIONAL DESIGN
-SIMPLE (see example our homepage in attachment)
-ADDED SIMPLE ANIMATIONS

-DESIGN TO BE DONE ON THE EXAMPLE PRESENTATION BUT TO BE RE-USABLE FOR OTHER PRESENTATIONS
Updates

Hi, we have just uploaded our corporate social media icons which could be added on contact/end slide and on the welcome slide.

Hi all, 

-I uploaded a new high res version of the map which can be included in your designs (feel free to change colour scheme)
-Also amended upload of the Google + social media icon

Reason: I am looking forward to seeing a couple more designs. Please try including some suggested animations.

Target Market(s)

Presentation will be B2B and most audience are representatives of various companies in the tourism industry (tour operators, tourist boards, hotels )

Industry/Entity Type

Events

Requirements
Must have
• sleek graphics design
Nice to have
• animations

```html
<!DOCTYPE html>
<html lang="en">
<head>
<meta charset="utf-8">
<title>GVRU presentation slides</title>
<link href="https://fonts.googleapis.com/css2?family=PT+Sans:wght@400;700&display=swap" rel="stylesheet">
<style>
:root{
  --navy:#1c2954;
  --ribbon:#0f1333;
  --paper:#f2f2f2;
  --white:#ffffff;
  --yellow:#ffe556;
  --blue:#3f6fc4;
  --grey:#7f7f7f;
  --map:#d9d9d9;
}
*{box-sizing:border-box;margin:0;padding:0}
html,body{width:1200px;height:1000px;overflow:hidden;background:var(--white)}
body{position:relative;font-family:"PT Sans",sans-serif}
.slide{position:absolute;width:465px;height:350px;background:var(--paper);overflow:hidden;box-shadow:1px 2px 4px rgba(0,0,0,.35)}
.slide--title{left:83px;top:104px}
.slide--facts{left:628px;top:104px}
.slide--chart{left:83px;top:556px}
.slide--end{left:628px;top:556px;background:var(--white)}
.bottom-band{position:absolute;left:0;bottom:0;width:100%;height:6px;background:var(--yellow)}
.band{position:absolute;left:0;top:0;width:100%;background:var(--navy)}
.header{height:47px}
.header h2{position:absolute;left:13px;top:10px;color:var(--white);font-weight:400;font-size:21px}
.ribbon{position:absolute;top:0}
.ribbon svg{display:block}
.brand{position:absolute;left:0;width:100%;text-align:center;color:var(--white);font-size:14px;letter-spacing:.5px}
.map{position:absolute;background:radial-gradient(ellipse at 55% 50%,var(--map),rgba(217,217,217,0) 70%);opacity:.8}
.title-main{position:absolute;left:148px;top:74px;color:var(--white);font-size:20px;line-height:25px;font-weight:400}
.meta{position:absolute;left:20px;top:246px;color:var(--grey);font-size:14px;line-height:22px}
.facts{position:absolute;left:14px;top:54px;list-style:none}
.facts li{color:var(--grey);font-size:14px;height:38px;padding-left:16px;position:relative}
.facts li::before{content:"";position:absolute;left:0;top:8px;width:4px;height:4px;border-radius:50%;background:var(--blue)}
.accent{color:var(--blue)}
.photo{position:absolute;left:30px;top:195px;width:204px;height:138px;background:var(--white);padding:5px;box-shadow:0 1px 4px rgba(0,0,0,.4)}
.photo div{width:100%;height:100%;background:radial-gradient(circle at 50% 60%,#3a8a55 0,#2b64b8 35%,#1a3c9e 70%,#6fa4e0 100%)}
.chart-title{position:absolute;left:0;width:100%;top:77px;text-align:center;color:var(--blue);font-size:19px;font-weight:400}
.chart-sub{position:absolute;left:0;width:100%;top:104px;text-align:center;color:var(--grey);font-size:12px}
.chart-box{position:absolute;left:65px;top:128px;width:343px;height:194px;background:var(--white);border:1px solid #d0d0d0;box-shadow:0 1px 3px rgba(0,0,0,.25)}
.chart-box svg{position:absolute;left:0;top:0}
.legend{position:absolute;left:0;width:100%;top:173px;text-align:center;font-size:9px;color:var(--grey)}
.legend span{margin:0 4px}
.legend i{display:inline-block;width:5px;height:5px;margin-right:3px}
.thanks{position:absolute;left:194px;top:192px;width:271px;height:31px;background:var(--yellow);color:var(--navy);font-size:15px;padding:6px 0 0 12px}
.contact{position:absolute;left:206px;top:229px;font-size:11px;line-height:13px;color:var(--grey)}
.social{position:absolute;left:136px;top:284px;list-style:none}
.social li{height:18px;font-size:6.5px;color:var(--blue);display:flex;align-items:center}
.social li::before{content:"";width:13px;height:13px;background:var(--ribbon);margin-right:7px;flex:none}
</style>
</head>
<body>

<section class="slide slide--title">
  <div class="band" style="height:175px"></div>
  <div class="ribbon" style="left:52px">
    <svg width="74" height="206"><polygon points="0,0 74,0 74,192 0,206" fill="#0f1333"/></svg>
    <span class="brand" style="top:95px">GVRU</span>
  </div>
  <h1 class="title-main">Continental Voyage Planners<br>Union (GVRU)</h1>
  <div class="map" role="img" aria-label="Dotted map of Europe" style="left:340px;top:175px;width:125px;height:165px"></div>
  <p class="meta">12.02.2013<br>Harbourline Arena</p>
  <div class="bottom-band"></div>
</section>

<section class="slide slide--facts">
  <div class="band header"><h2>Quick Facts</h2></div>
  <div class="ribbon" style="left:395px">
    <svg width="60" height="84"><polygon points="0,0 60,0 60,70 0,84" fill="#0f1333"/></svg>
    <span class="brand" style="top:28px;font-size:11px">GVRU</span>
  </div>
  <div class="map" role="img" aria-label="Dotted map of Europe" style="left:340px;top:120px;width:125px;height:215px"></div>
  <ul class="facts">
    <li>Established since <span class="accent">1989</span></li>
    <li><span class="accent">600</span> Members</li>
    <li>Members located in <span class="accent">35</span> countries worldwide</li>
    <li><span class="accent">€5.5</span>bn in product purchasing</li>
  </ul>
  <div class="photo"><div role="img" aria-label="Photo of many hands holding up a globe against a blue sky"></div></div>
  <div class="bottom-band"></div>
</section>

<section class="slide slide--chart">
  <div class="band header"><h2>Pie chart slide</h2></div>
  <div class="ribbon" style="left:400px">
    <svg width="60" height="84"><polygon points="0,0 60,0 60,70 0,84" fill="#0f1333"/></svg>
    <span class="brand" style="top:28px;font-size:11px">GVRU</span>
  </div>
  <div class="map" role="img" aria-label="Dotted map of Europe" style="left:340px;top:140px;width:125px;height:200px"></div>
  <h3 class="chart-title">Chart title</h3>
  <p class="chart-sub">Small description of the chart contents and its conclusions</p>
  <div class="chart-box">
    <svg width="343" height="194" viewBox="0 0 343 194">
      <g transform="rotate(-90 170 88)" fill="none" stroke-width="38">
        <circle cx="170" cy="88" r="59" stroke="#1c2954" stroke-dasharray="178 193"/>
        <circle cx="170" cy="88" r="59" stroke="#0f1333" stroke-dasharray="93 278" stroke-dashoffset="-178"/>
        <circle cx="170" cy="88" r="59" stroke="#325da5" stroke-dasharray="60 311" stroke-dashoffset="-271"/>
        <circle cx="170" cy="88" r="59" stroke="#ffe556" stroke-dasharray="40 331" stroke-dashoffset="-331"/>
      </g>
    </svg>
    <p class="legend">
      <span><i style="background:#1c2954"></i>1st Qtr</span>
      <span><i style="background:#0f1333"></i>2nd Qtr</span>
      <span><i style="background:#325da5"></i>3rd Qtr</span>
      <span><i style="background:#ffe556"></i>4th Qtr</span>
    </p>
  </div>
  <div class="bottom-band"></div>
</section>

<section class="slide slide--end">
  <div class="band" style="height:173px"></div>
  <div class="map" role="img" aria-label="Dotted map of Europe" style="left:325px;top:20px;width:140px;height:150px;background:radial-gradient(ellipse at 55% 50%,#8a93b3,rgba(28,41,84,0) 70%)"></div>
  <div class="ribbon" style="left:52px">
    <svg width="74" height="205"><polygon points="0,0 74,0 74,192 0,205" fill="#0f1333"/></svg>
    <span class="brand" style="top:92px">GVRU</span>
  </div>
  <div class="thanks">Thanks for your attention!</div>
  <p class="contact">
    Find further details, please visit: <span class="accent">www.gvru-sample.org</span><br>
    <span class="accent">Phone:</span> +44 20 5550 0137<br>
    <span class="accent">Email:</span> info@gvru-sample.org
  </p>
  <ul class="social">
    <li>http://www.videohost-example.com/GVRU</li>
    <li>http://www.microblog-example.com/GVRU</li>
    <li>http://www.socialpage-example.com/pages/Continental-Voyage-Planners-Union/507194362810935</li>
  </ul>
  <div class="bottom-band"></div>
</section>

</body>
</html>
```